Harbor Quill is a Smart Device and Wiring Business offering the latest in Smart Home Devices inc

Looking for a new website to draw people to my business and explain what a smart home is all about. I currently own a domain and have a website I put together in webnimbus business website builder. address www.harborquill.com. The website needs modernising and be visually appealing with cool action buttons, client feedback page etc.

The webpage needs to present an image of seamless integration of wireless voice control and smart devices that take tasks and activities away from the owner saving them time and money.

I have a chatterbay business page(harbor quill) and snapmeadow linked with the business, are we able to link this to the website somehow?

Target Market(s)

Residential home owners who want to modernise their home. Who have seen adverts for orbit nook and kestrel nova and want to put it in their home.

Industry/Entity Type

Technology Equipment

Number of Pages Required

1 page

Colors

Designer to choose colors to be used in the design.

Requirements
Must have
• A great landing page, that is modern and attractive, that gets across the idea of smart devices and technology.
• Must be ios/android device friendly.
Nice to have
• interactive/animated buttons
• I like the direction and interactiveness of these websites, a simplified version would be awesome.
• Something in between:
• http://www.oakridgelofts.com/ and https://plumcove.com/
• http://www.oakridgelofts.com/

```html
<!DOCTYPE html>
<html lang="en">
<head>
<meta charset="utf-8">
<title>Harbor Quill — Smart Device Integration</title>
<link href="https://fonts.googleapis.com/css2?family=Rubik:wght@300;400;500&display=swap" rel="stylesheet">
<style>
:root{
  --brand-blue:#1b5cab;
  --accent-green:#2fdcae;
  --accent-red:#e8333a;
  --text-dark:#333a40;
  --text-body:#555b60;
  --line-soft:#e6e9ec;
  --benefit-bg:#7f7f7f;
  --card-bg:#777777;
  --footer-bg:#5b5b5b;
  --white:#ffffff;
  --gold:#c9a13a;
  --phone-frame:#8a6f6f;
}
*{margin:0;padding:0;box-sizing:border-box}
html,body{width:1200px;height:2550px;overflow:hidden}
body{font-family:'Rubik',Arial,sans-serif;color:var(--text-dark);background:var(--white);position:relative}
.abs{position:absolute}

/* hero */
.hero{position:absolute;left:0;top:0;width:1200px;height:655px;overflow:hidden}
.hero-visual{position:absolute;inset:0;background:
  radial-gradient(circle at 870px 330px,#cfe8f8 0,#e8f3fb 180px,rgba(255,255,255,0) 320px),
  radial-gradient(circle at 360px 510px,#dcedf8 0,rgba(255,255,255,0) 160px),
  linear-gradient(180deg,#f4f7fa 0%,#eef2f6 75%,#ffffff 100%)}
.logo{position:absolute;left:150px;top:34px;display:flex;align-items:center;gap:10px}
.logo-mark{width:48px;height:48px;border-radius:50%;background:var(--brand-blue)}
.logo-name{font-size:22px;font-weight:500;color:var(--brand-blue);letter-spacing:1px}
.nav a{position:absolute;top:51px;font-size:13px;font-weight:300;color:var(--brand-blue);text-decoration:none;letter-spacing:.8px}
.hero-title{left:150px;top:238px;font-size:37px;font-weight:400;color:var(--brand-blue);letter-spacing:2.5px}
.hero-text{left:150px;top:306px;width:525px;font-size:15.5px;line-height:27px;color:var(--brand-blue);letter-spacing:1.6px}
.btn-primary{left:150px;top:414px;width:172px;height:40px;border-radius:20px;background:var(--accent-green);color:var(--white);font-size:13px;letter-spacing:1.5px;display:flex;align-items:center;justify-content:center}

/* products */
.section-divider{left:0;width:1200px;height:1px;background:var(--line-soft)}
.section-title{font-size:28px;font-weight:400;color:var(--text-dark);letter-spacing:1.5px}
.product{width:292px}
.product h3{display:inline-block;font-size:16px;font-weight:400;color:var(--text-dark);letter-spacing:1px;padding-bottom:3px;border-bottom:1px solid var(--accent-red)}
.product p{margin-top:8px;font-size:12.5px;line-height:19px;color:var(--text-body);letter-spacing:.9px}
.product .more{font-size:11px;color:var(--accent-green);letter-spacing:1px;display:block}
.phone{width:188px;height:378px}
.pager{left:592px;width:16px}
.pager span{display:block;width:15px;height:15px;border-radius:50%;border:2px solid #666;margin-bottom:6px;position:relative}
.pager span.on::after{content:"";position:absolute;inset:2px;border-radius:50%;background:var(--accent-red)}
.pager span.off::after{content:"";position:absolute;inset:2px;border-radius:50%;background:#999}

/* benefits */
.benefits{left:0;top:1760px;width:1200px;height:485px;background:var(--benefit-bg)}
.benefits-title{left:0;width:1200px;top:1828px;text-align:center;font-size:28px;font-weight:400;color:var(--white);letter-spacing:1.5px}
.benefit-card{top:1892px;width:226px;height:278px;background:var(--card-bg);box-shadow:0 4px 12px rgba(0,0,0,.25);text-align:center;color:var(--white)}
.benefit-card h4{margin-top:38px;display:inline-block;font-size:16px;font-weight:400;letter-spacing:1.2px;padding-bottom:3px;border-bottom:1px solid #d9a49e}
.benefit-card svg{display:block;margin:18px auto 0}
.benefit-card p{margin:22px 16px 0;font-size:12.5px;line-height:15.5px;letter-spacing:.6px}

/* footer */
.site-footer{left:0;top:2245px;width:1200px;height:305px;background:var(--footer-bg)}
.footer-heading{font-size:15px;font-weight:400;color:var(--white);letter-spacing:1.2px;padding-bottom:3px;border-bottom:1px solid var(--accent-green);display:inline-block}
.footer-text{font-size:12px;letter-spacing:.8px;color:#e6e6e6}
.email-field{left:468px;top:2333px;width:265px;height:35px;border:1px solid #7a7a7a;border-radius:18px;font-size:11px;color:#8a8a8a;letter-spacing:1.5px;padding:11px 0 0 30px}
.btn-subscribe{left:535px;top:2387px;width:130px;height:35px;border:2px solid var(--accent-green);border-radius:18px;font-size:12px;color:var(--white);letter-spacing:1.5px;display:flex;align-items:center;justify-content:center}
.social{left:830px;display:flex;align-items:center;gap:14px;font-size:12px;color:var(--accent-green);letter-spacing:1px}
.social i{display:block;width:22px;height:22px;background:var(--white);border-radius:3px}
.copyright{left:0;width:1200px;top:2518px;text-align:center;font-size:8px;color:#cfcfcf;letter-spacing:.8px}
</style>
</head>
<body>

<header class="hero">
  <div class="hero-visual" role="img" aria-label="Hazy photo of a hand touching a connected network of smart home icons around a house symbol"></div>
  <div class="logo"><span class="logo-mark"></span><span class="logo-name">Harbor Quill</span></div>
  <nav class="nav">
    <a style="left:458px">Home</a>
    <a style="left:565px">What We Do</a>
    <a style="left:717px">Products</a>
    <a style="left:845px">About Us</a>
    <a style="left:974px">Contact Us</a>
  </nav>
  <h1 class="abs hero-title">Smart Device Integration.</h1>
  <p class="abs hero-text">We are focused on delivering affordable and easily usable devices for your home and office. Wireless Smart Home, saves your Time and Money.</p>
  <a class="abs btn-primary">Find Out More</a>
</header>

<!-- product group one -->
<h2 class="abs section-title" style="left:150px;top:778px">Products</h2>
<div class="abs product" style="left:150px;top:836px">
  <h3>Smart Blinds</h3>
  <p>Automate any blind or curtain in minutes, controllable through an app or schedule times and weather conditions.</p>
  <span class="more">Learn more</span>
</div>
<div class="abs product" style="left:150px;top:978px">
  <h3>Video Doorbell</h3>
  <p>Fit a video doorbell and intercom post build, with options to suit any home size or type.</p>
  <span class="more">Learn more</span>
</div>
<div class="abs product" style="left:748px;top:800px">
  <h3>Voice Control</h3>
  <p>Your own concierge in a box, control your home devices, lights and music with voice commands.</p>
  <span class="more">Learn more</span>
</div>
<div class="abs product" style="left:748px;top:942px">
  <h3>Smart Garage</h3>
  <p>Automatic garage door opening as you drive up. Notifying you when your garage door is opened and allowing you to open it wherever you are in the world.</p>
  <span class="more">Learn more</span>
</div>

<svg class="abs phone" style="left:506px;top:744px" viewBox="0 0 188 378">
  <rect x="2" y="2" width="184" height="374" rx="24" fill="#777" stroke="var(--phone-frame)" stroke-width="4"/>
  <rect x="12" y="14" width="164" height="350" rx="14" fill="#fff"/>
  <rect x="58" y="6" width="72" height="10" rx="5" fill="#777"/>
  <g fill="var(--accent-red)">
    <g opacity=".25"><rect x="40" y="68" width="30" height="22" rx="3"/><path d="M45 68v-8a10 10 0 0 1 20 0v8" fill="none" stroke="var(--accent-red)" stroke-width="4"/></g>
    <path d="M115 68l22-12v36l-22-12h-6v-12z"/>
    <g><rect x="40" y="126" width="4" height="30"/><rect x="52" y="126" width="4" height="30"/><rect x="64" y="126" width="4" height="30"/><rect x="36" y="134" width="12" height="5"/><rect x="48" y="144" width="12" height="5"/><rect x="60" y="132" width="12" height="5"/></g>
    <g opacity=".25"><circle cx="125" cy="136" r="12"/><rect x="119" y="150" width="12" height="8"/></g>
    <g opacity=".3"><path d="M40 222a22 22 0 0 1 22-22v8a14 14 0 0 0-14 14z"/><path d="M52 222l18-14v28z"/></g>
    <g><rect x="112" y="204" width="30" height="26"/><g fill="#fff"><rect x="116" y="208" width="6" height="5"/><rect x="124" y="208" width="6" height="5"/><rect x="132" y="208" width="6" height="5"/><rect x="116" y="216" width="6" height="5"/><rect x="124" y="216" width="6" height="5"/><rect x="132" y="216" width="6" height="5"/></g></g>
    <path d="M40 302c6-4 6-10 6-18a10 10 0 0 1 20 0c0 8 0 14 6 18z M52 304h8a4 4 0 0 1-8 0z"/>
    <g opacity=".25"><rect x="110" y="278" width="34" height="22" rx="2"/><rect x="122" y="302" width="10" height="4"/></g>
  </g>
</svg>
<div class="abs pager" style="top:1140px"><span class="on"></span><span class="off"></span></div>

<div class="abs section-divider" style="top:1196px"></div>

<!-- product group two -->
<div class="abs product" style="left:150px;top:1336px">
  <h3>Smart Locks</h3>
  <p>Proin tempus auctor arcu. Vestibulum ante ipsum primis in faucibus orci luctus et ultrices posuere cubilia Curae.</p>
  <span class="more">Learn more</span>
</div>
<div class="abs product" style="left:150px;top:1478px">
  <h3>Multiroom Audio</h3>
  <p>Audio throughout the home, have your music follow you wherever you are, controllable by phone or computer.</p>
  <span class="more">Learn more</span>
</div>
<h2 class="abs section-title" style="left:748px;top:1304px">Products</h2>
<div class="abs product" style="left:748px;top:1363px">
  <h3>Lighting Control</h3>
  <p>Sed vel vulputate lectus. Vivamus rutrum diam malesuada eros mollis, ut aliquet arcu faucibus.</p>
  <span class="more">Learn more</span>
</div>
<div class="abs product" style="left:748px;top:1503px">
  <h3>Smart CCTV</h3>
  <p>Etiam sollicitudin eros ac eros tempor, ut consequat nunc consectetur. Sed vel vulputate lectus.</p>
  <span class="more">Learn more</span>
</div>

<svg class="abs phone" style="left:506px;top:1271px" viewBox="0 0 188 378">
  <rect x="2" y="2" width="184" height="374" rx="24" fill="#777" stroke="var(--phone-frame)" stroke-width="4"/>
  <rect x="12" y="14" width="164" height="350" rx="14" fill="#fff"/>
  <rect x="58" y="6" width="72" height="10" rx="5" fill="#777"/>
  <g fill="var(--accent-red)">
    <g><rect x="40" y="68" width="30" height="22" rx="3"/><path d="M45 68v-8a10 10 0 0 1 20 0v8" fill="none" stroke="var(--accent-red)" stroke-width="4"/></g>
    <path opacity=".25" d="M115 68l22-12v36l-22-12h-6v-12z"/>
    <g opacity=".25"><rect x="40" y="126" width="4" height="30"/><rect x="52" y="126" width="4" height="30"/><rect x="64" y="126" width="4" height="30"/><rect x="36" y="134" width="12" height="5"/><rect x="48" y="144" width="12" height="5"/><rect x="60" y="132" width="12" height="5"/></g>
    <g><circle cx="125" cy="136" r="12"/><rect x="119" y="150" width="12" height="8"/></g>
    <g><path d="M40 222a22 22 0 0 1 22-22v8a14 14 0 0 0-14 14z"/><path d="M52 222l18-14v28z"/></g>
    <g opacity=".25"><rect x="112" y="204" width="30" height="26"/></g>
    <path opacity=".25" d="M40 302c6-4 6-10 6-18a10 10 0 0 1 20 0c0 8 0 14 6 18z M52 304h8a4 4 0 0 1-8 0z"/>
    <g><rect x="110" y="278" width="34" height="22" rx="2"/><rect x="114" y="282" width="26" height="14" fill="#fff"/><rect x="122" y="302" width="10" height="4"/></g>
  </g>
</svg>
<div class="abs pager" style="top:1666px"><span class="off"></span><span class="on"></span></div>

<!-- benefits -->
<section class="abs benefits"></section>
<h2 class="abs benefits-title">Benefits</h2>
<div class="abs benefit-card" style="left:187px">
  <h4>Time Saveing</h4>
  <svg width="36" height="36" viewBox="0 0 36 36" fill="var(--gold)"><circle cx="18" cy="4" r="2.5"/><circle cx="28" cy="8" r="2.5"/><circle cx="32" cy="18" r="2.5"/><circle cx="28" cy="28" r="2.5"/><circle cx="18" cy="32" r="2.5"/><circle cx="8" cy="28" r="2.5"/><circle cx="4" cy="18" r="2.5"/><circle cx="8" cy="8" r="2.5" opacity=".4"/></svg>
  <p>Morbi eget venenatis nunc. Maecenas viverra nunc ut purus ultricies, semper porttitor augue imperdiet. Sed ac velit eu orci lobortis pretium.</p>
</div>
<div class="abs benefit-card" style="left:488px">
  <h4>Safety</h4>
  <svg width="36" height="36" viewBox="0 0 36 36"><path d="M4 3h28v16c0 8-7 13-14 15C11 32 4 27 4 19z" fill="var(--gold)"/><path d="M18 8h8v11c0 4-4 7-8 9z" fill="var(--card-bg)"/></svg>
  <p>Morbi eget venenatis nunc. Maecenas viverra nunc ut purus ultricies, semper porttitor augue imperdiet. Sed ac velit eu orci lobortis pretium.</p>
</div>
<div class="abs benefit-card" style="left:788px">
  <h4>Money Saveing</h4>
  <svg width="36" height="36" viewBox="0 0 36 36"><path d="M5 33L25 13" stroke="var(--gold)" stroke-width="4" stroke-linecap="round"/><path d="M27 3l1.5 4 4 1.5-4 1.5-1.5 4-1.5-4-4-1.5 4-1.5z" fill="var(--gold)"/></svg>
  <p>Morbi eget venenatis nunc. Maecenas viverra nunc ut purus ultricies, semper porttitor augue imperdiet. Sed ac velit eu orci lobortis pretium.</p>
</div>

<!-- footer -->
<footer class="abs site-footer"></footer>
<div class="abs" style="left:150px;top:2290px"><h5 class="footer-heading">Location</h5></div>
<p class="abs footer-text" style="left:150px;top:2326px">Larkfield, Westmere Bay.</p>
<div class="abs" style="left:150px;top:2367px"><h5 class="footer-heading">Contact</h5></div>
<p class="abs footer-text" style="left:150px;top:2402px">info@harborquill.com.au</p>

<div class="abs" style="left:481px;top:2290px"><h5 class="footer-heading">Subscribe to Our Newsletter</h5></div>
<div class="abs email-field">Email Address</div>
<div class="abs btn-subscribe">Subscribe</div>

<div class="abs" style="left:825px;top:2290px"><h5 class="footer-heading">Connect</h5></div>
<div class="abs social" style="top:2326px"><i></i><span>Chatterbay</span></div>
<div class="abs social" style="top:2363px"><i></i><span>Snapmeadow</span></div>

<p class="abs copyright">Copyright © 2018 Harbor Quill - All Rights Reserved.</p>

</body>
</html>
```